Orchards Beneath the Tide book cover design

Book cover - the book contains 52 chapters - 2 for each letter of the alphabet, so a yearlong focus on Leadership. The Intent is to communicate that leadership is common sense. It just isn’t common practice. This book allows the reader to focus on one leadership word each week for a yearlong focus on improving one’s leadership. It is full of stories relating to the 52 words that will challenge and inspire the reader.
Target Market(s)
Leaders / Emerging Leaders
Industry/Entity Type
All
Requirements
Must have
- Appeal to executives
Nice to have
- Simplicity
Should not have
- Cartoon feel

```html
<!DOCTYPE html>
<html lang="en">
<head>
<meta charset="utf-8">
<title>Orchards Beneath the Tide — Book Cover</title>
<link rel="stylesheet" href="https://fonts.googleapis.com/css2?family=Barlow+Condensed:wght@700&family=Plus+Jakarta+Sans:wght@300;700&display=swap">
<style>
  :root {
    --page-bg: #ffffff;
    --cover-bg: #1b1a18;
    --title-orange: #ff8a10;
    --title-yellow: #f3d44e;
    --ink-white: #ffffff;
    --glow-core: #fff6c8;
    --glow-warm: #f0a43a;
    --glow-deep: #7a4a12;
  }
  html, body {
    margin: 0;
    padding: 0;
    width: 1200px;
    height: 1200px;
    overflow: hidden;
    background: var(--page-bg);
  }
  .book-cover {
    position: absolute;
    left: 242px;
    top: 64px;
    width: 715px;
    height: 1072px;
    background: var(--cover-bg);
  }
  .book-cover svg {
    display: block;
    width: 100%;
    height: 100%;
  }
  .title-display {
    font-family: "Barlow Condensed", "Arial Narrow", sans-serif;
    font-weight: 700;
  }
  .subtitle {
    font-family: "Plus Jakarta Sans", Arial, sans-serif;
    font-weight: 300;
    font-size: 20px;
    fill: var(--ink-white);
  }
  .author-name {
    font-family: "Plus Jakarta Sans", Arial, sans-serif;
    font-weight: 700;
    font-size: 44px;
    letter-spacing: -1.5px;
    fill: var(--ink-white);
  }
</style>
</head>
<body>
  <div class="book-cover">
    <svg viewBox="0 0 715 1072" xmlns="http://www.w3.org/2000/svg">
      <defs>
        <linearGradient id="doorway-glow" x1="0" y1="0" x2="1" y2="0">
          <stop offset="0" stop-color="#1b1a18"/>
          <stop offset="0.30" stop-color="#3a2612"/>
          <stop offset="0.38" stop-color="var(--glow-deep)"/>
          <stop offset="0.42" stop-color="var(--glow-warm)"/>
          <stop offset="0.44" stop-color="#f6e08a"/>
          <stop offset="0.50" stop-color="var(--glow-core)"/>
          <stop offset="0.56" stop-color="#f6e08a"/>
          <stop offset="0.58" stop-color="var(--glow-warm)"/>
          <stop offset="0.62" stop-color="var(--glow-deep)"/>
          <stop offset="0.70" stop-color="#3a2612"/>
          <stop offset="1" stop-color="#1b1a18"/>
        </linearGradient>
        <linearGradient id="scene-fade" x1="0" y1="0" x2="0" y2="1">
          <stop offset="0" stop-color="#1b1a18" stop-opacity="0"/>
          <stop offset="0.7" stop-color="#1b1a18" stop-opacity="0.35"/>
          <stop offset="1" stop-color="#1b1a18" stop-opacity="1"/>
        </linearGradient>
      </defs>

      <rect class="cover-ground" width="715" height="1072" fill="var(--cover-bg)"/>

      <g class="cover-illustration" role="img" aria-label="Illustration: a figure raising a trophy in a tall glowing doorway at the top of dark steps">
        <rect x="0" y="0" width="715" height="470" fill="url(#doorway-glow)"/>
        <rect x="0" y="0" width="715" height="470" fill="url(#scene-fade)"/>
      </g>

      <text class="title-display title-main" x="357.5" y="596" text-anchor="middle"
            font-size="150" fill="var(--title-orange)"
            textLength="585" lengthAdjust="spacing">ORCHARDS</text>

      <g class="title-connector">
        <line x1="64" y1="628" x2="198" y2="628" stroke="var(--ink-white)" stroke-width="1.2"/>
        <text class="title-display" x="357.5" y="643" text-anchor="middle"
              font-size="43" fill="var(--title-yellow)">BENEATH THE</text>
        <line x1="517" y1="628" x2="651" y2="628" stroke="var(--ink-white)" stroke-width="1.2"/>
      </g>

      <text class="title-display title-final" x="357.5" y="835" text-anchor="middle"
            font-size="258" fill="var(--ink-white)"
            textLength="585" lengthAdjust="spacing">TIDE</text>

      <text class="subtitle" text-anchor="middle">
        <tspan x="357.5" y="918">Focus on One Leadership Word Each Week For a Year</tspan>
        <tspan x="357.5" y="948">Long Focus on Improving One’s Leadership.</tspan>
      </text>

      <text class="author-name" x="357.5" y="1028" text-anchor="middle">AUTHOR NAME HERE</text>
    </svg>
  </div>
</body>
</html>
```